A Lowen Grad

This poster is to show how we want the world to view our high school students when the graduate. The values and lessons they should live by.
I'd like for the middle to say "A LOWEN GRAD IS..." and it should be surrounded by the following values:
Never Quits
Doesn't Put Others Down
Respects Everyone
Learns from their mistakes
Takes action
Always looks to Improve
Looks to the future
Puts others' needs before our own

and the final emotion one should have more emphasis....
will always be a part of Lowen

I want it to look cool and sleek, not just listed out. Maybe a thought bubble or something like that. Please use school colors and use the school logo

```html
<!DOCTYPE html>
<html lang="en">
<head>
<meta charset="utf-8">
<title>A Lowen Grad</title>
<link href="https://fonts.googleapis.com/css2?family=Poppins:wght@700;800&family=Jost:wght@500&display=swap" rel="stylesheet">
<style>
  :root {
    --navy: #1f1f5e;
    --navy-deep: #18185a;
    --violet: #4c4a80;
    --glow-blue: #2d5c93;
    --gold: #eeb312;
    --sky: #17a4dc;
    --orange: #e8901f;
    --paper: #f2f1f5;
    --white: #ffffff;
  }
  * { box-sizing: border-box; margin: 0; padding: 0; }
  html, body { width: 992px; height: 1200px; overflow: hidden; background: var(--navy); }
  .poster {
    position: relative;
    width: 992px;
    height: 1200px;
    overflow: hidden;
    background:
      radial-gradient(ellipse 420px 520px at 20px 450px, rgba(60,120,180,0.55), transparent 70%),
      radial-gradient(ellipse 600px 700px at 950px 150px, rgba(110,105,160,0.6), transparent 70%),
      radial-gradient(ellipse 500px 500px at 800px 950px, rgba(150,110,80,0.45), transparent 70%),
      linear-gradient(160deg, var(--navy-deep) 0%, var(--navy) 55%, #2a2460 100%);
  }
  .mascot-art {
    position: absolute;
    left: 330px;
    top: 360px;
    width: 600px;
    height: 830px;
    border-radius: 48% 40% 30% 50%;
    background: radial-gradient(ellipse at 55% 50%, rgba(30,30,98,0.95) 0%, rgba(30,30,98,0.7) 50%, transparent 72%);
  }
  .quote-mark {
    position: absolute;
    left: 110px;
    top: 40px;
    font-family: "Poppins", sans-serif;
    font-weight: 800;
    font-size: 170px;
    line-height: 1;
    color: var(--gold);
  }
  .cap-icon { position: absolute; left: 262px; top: 128px; width: 130px; height: 70px; }
  .headline {
    position: absolute;
    left: 108px;
    top: 160px;
    font-family: "Poppins", sans-serif;
    font-weight: 700;
    font-size: 104px;
    line-height: 1;
    letter-spacing: -2px;
  }
  .headline .line-one { display: block; color: var(--white); }
  .headline .accent { color: var(--gold); }
  .headline .line-two { display: block; margin: 8px 0 0 288px; color: var(--gold); }
  .headline .dots { color: var(--white); }
  .school-ribbon {
    position: absolute;
    left: 741px;
    top: 0;
    width: 154px;
    height: 208px;
    background: var(--paper);
    clip-path: polygon(0 0, 100% 0, 100% 100%, 50% 82%, 0 100%);
    display: flex;
    flex-direction: column;
    align-items: center;
    padding-top: 58px;
    gap: 10px;
  }
  .school-ribbon .mark { width: 44px; height: 44px; border-radius: 50%; background: var(--gold); }
  .school-ribbon .name { font-family: "Jost", sans-serif; font-weight: 500; font-size: 22px; color: var(--navy); }
  .values { position: absolute; left: 112px; top: 372px; list-style: none; }
  .value { display: flex; align-items: center; height: 85px; }
  .value .dot {
    width: 62px; height: 62px; border-radius: 50%;
    background: var(--paper);
    border: 6px solid #d9d7e0;
    flex: none;
  }
  .bubble {
    position: relative;
    margin-left: 29px;
    margin-top: -10px;
    padding: 0 32px;
    height: 56px;
    line-height: 56px;
    border-radius: 28px;
    font-family: "Jost", sans-serif;
    font-weight: 500;
    font-size: 29px;
    white-space: nowrap;
  }
  .bubble::after {
    content: "";
    position: absolute;
    left: 28px;
    bottom: -20px;
    border-top: 22px solid currentColor;
    border-right: 24px solid transparent;
    color: inherit;
  }
  .bubble.light { background: var(--paper); color: var(--navy); }
  .bubble.light::after { border-top-color: var(--paper); }
  .bubble.sky { background: var(--sky); color: var(--white); }
  .bubble.sky::after { border-top-color: var(--sky); }
  .bubble.emphasis { background: var(--orange); color: var(--navy); font-size: 33px; height: 60px; line-height: 60px; }
  .bubble.emphasis::after { border-top-color: var(--orange); }
  .web-address {
    position: absolute;
    left: 796px;
    top: 1142px;
    font-family: "Poppins", sans-serif;
    font-weight: 700;
    font-size: 18px;
    color: #e6e4ee;
    letter-spacing: 0.5px;
  }
  .base-band { position: absolute; left: 0; bottom: 0; width: 100%; height: 15px; background: var(--gold); }
</style>
</head>
<body>
<main class="poster">
  <div class="mascot-art" role="img" aria-label="Large dark silhouette of the school mascot bird wearing a graduation cap"></div>

  <div class="quote-mark">“</div>
  <svg class="cap-icon" viewBox="0 0 130 70" aria-hidden="true">
    <polygon points="10,30 70,5 125,28 65,52" fill="#ffffff"/>
    <path d="M38 40 L38 58 Q65 72 92 58 L92 40 L65 52 Z" fill="#e9e9ee"/>
    <line x1="65" y1="28" x2="100" y2="38" stroke="#1f1f5e" stroke-width="2"/>
    <line x1="100" y1="38" x2="100" y2="62" stroke="#1f1f5e" stroke-width="2"/>
  </svg>

  <h1 class="headline">
    <span class="line-one">A <span class="accent">Lowen</span></span>
    <span class="line-two">Grad<span class="dots">....</span></span>
  </h1>

  <div class="school-ribbon">
    <span class="mark"></span>
    <span class="name">Lowen</span>
  </div>

  <ul class="values">
    <li class="value"><span class="dot"></span><span class="bubble light">Never Quits</span></li>
    <li class="value"><span class="dot"></span><span class="bubble sky">Doesn’t Put Others Down</span></li>
    <li class="value"><span class="dot"></span><span class="bubble light">Respects Everyone</span></li>
    <li class="value"><span class="dot"></span><span class="bubble sky">Learns From Their Mistakes</span></li>
    <li class="value"><span class="dot"></span><span class="bubble light">Takes Action</span></li>
    <li class="value"><span class="dot"></span><span class="bubble sky">Always Looks To Improve</span></li>
    <li class="value"><span class="dot"></span><span class="bubble light">Looks To The Future</span></li>
    <li class="value"><span class="dot"></span><span class="bubble sky">Puts Others’ Needs Before Our Own</span></li>
    <li class="value"><span class="dot"></span><span class="bubble emphasis">Will Always Be A Part Of Lowen</span></li>
  </ul>

  <div class="web-address">WEBSITE.COM</div>
  <div class="base-band"></div>
</main>
</body>
</html>
```